PDF Document Update

Hi,

I need the attached PDF document updated.

The word document attached outlines the new format for which I want the PDF to look like.

For the "Our People" section - please remove Wilma Brackett and add in Owen Pellow (his photo is also attached).

Thanks!

```html
<!DOCTYPE html>
<html lang="en">
<head>
<meta charset="utf-8">
<title>Our People – Keller Careers</title>
<link href="https://fonts.googleapis.com/css2?family=Rubik:wght@300;400;500;800&display=swap" rel="stylesheet">
<style>
  :root {
    --navy: #1d4289;
    --navy-soft: #a5b4d2;
    --grey-wave: #cfcfd1;
    --ink: #222433;
    --body: #55565f;
    --white: #ffffff;
  }
  * { margin: 0; padding: 0; box-sizing: border-box; }
  html, body { width: 849px; height: 1200px; overflow: hidden; background: var(--white); }
  .page {
    position: relative;
    width: 849px;
    height: 1200px;
    overflow: hidden;
    background: var(--white);
    font-family: "Rubik", sans-serif;
  }
  .header-art, .footer-art { position: absolute; left: 0; display: block; }
  .header-art { top: 0; }
  .footer-art { bottom: 0; }

  .section-title {
    position: absolute;
    left: 0;
    top: 244px;
    width: 568px;
    height: 76px;
    background: var(--navy);
    border-top-right-radius: 26px;
  }
  .section-title h1 {
    position: absolute;
    left: 223px;
    top: 9px;
    font-weight: 800;
    font-size: 48px;
    letter-spacing: -0.5px;
    color: var(--white);
    line-height: 1.2;
  }

  .person { position: absolute; left: 0; width: 849px; }
  .person--first { top: 350px; }
  .person--second { top: 778px; }
  .portrait {
    position: absolute;
    left: 38px;
    top: 0;
    width: 152px;
    height: 152px;
    border-radius: 50%;
    background: radial-gradient(circle at 50% 45%, #7d8fb0 0%, #3d5a45 55%, #1f3321 100%);
  }
  .bio { position: absolute; left: 224px; top: 0; width: 588px; }
  .bio h2 {
    font-weight: 500;
    font-size: 22.5px;
    color: var(--ink);
    line-height: 1.2;
    margin-bottom: 3px;
  }
  .bio p {
    font-weight: 300;
    font-size: 14.1px;
    line-height: 18px;
    color: var(--body);
    margin-bottom: 18px;
  }

  .contact-heading {
    position: absolute;
    right: 39px;
    top: 1116px;
    font-weight: 500;
    font-size: 22px;
    color: var(--white);
  }
  .contact-rule {
    position: absolute;
    left: 619px;
    top: 1146px;
    width: 197px;
    height: 1px;
    background: var(--white);
  }
  .contact-row { position: absolute; top: 1169px; left: 0; width: 849px; height: 23px; }
  .contact-item {
    position: absolute;
    display: flex;
    align-items: center;
    gap: 9px;
    color: var(--white);
    font-weight: 300;
    font-size: 12.5px;
    white-space: nowrap;
  }
  .contact-item svg { width: 23px; height: 23px; flex: none; }
  .contact-item--web { left: 33px; }
  .contact-item--mail { left: 219px; }
  .contact-item--pin { left: 417px; }
  .contact-item--phone { left: 679px; }
</style>
</head>
<body>
<div class="page">

  <svg class="header-art" width="849" height="320" viewBox="0 0 849 320">
    <defs>
      <linearGradient id="skyline" x1="0" y1="0" x2="0" y2="1">
        <stop offset="0" stop-color="#b9cbe0"/>
        <stop offset="0.35" stop-color="#9aa8a8"/>
        <stop offset="0.6" stop-color="#5a7aa0"/>
        <stop offset="1" stop-color="#3d6593"/>
      </linearGradient>
    </defs>
    <path role="img" aria-label="Photograph of the Sydney harbour skyline with the Opera House" fill="url(#skyline)"
      d="M0,0 H849 V205 C820,170 760,140 680,132 C560,118 420,122 300,125 C190,128 100,110 40,60 C20,42 8,22 0,8 Z"/>
    <path fill="var(--grey-wave)" d="M520,150 C660,128 780,150 820,210 C838,238 849,265 849,290 V205 C820,160 760,138 680,135 C620,132 570,140 520,150 Z"/>
    <path fill="var(--navy-soft)" d="M0,172 C60,200 140,210 230,205 C360,198 460,170 560,156 L600,152 C470,160 330,190 200,192 C110,194 40,178 0,160 Z"/>
    <path fill="var(--navy)" d="M0,28 C50,90 130,124 240,126 C380,128 520,108 660,108 C760,108 825,150 849,200 V212 C815,170 740,142 640,145 C500,150 360,190 220,190 C120,190 40,172 0,155 Z"/>
    <path fill="#f3d8e6" d="M0,0 C40,70 120,118 230,124 L240,126 C130,124 50,90 0,28 Z" opacity="0.7"/>
  </svg>

  <div class="section-title"><h1>OUR PEOPLE</h1></div>

  <section class="person person--first">
    <div class="portrait" role="img" aria-label="Portrait photo of Adrian Keller"></div>
    <div class="bio">
      <h2>Adrian Keller - Director/Founder</h2>
      <p>Adrian has 20+ years of financial services recruitment experience, with the past 19 years assisting clients across Asia Pacific with appointing senior infrastructure/middle office staff.</p>
      <p>After graduating from Harbourview University in Australia with a degree in Environmental Science, Adrian spent two years in London providing recruitment services to investment banks and fund managers across a broad range of finance disciplines.</p>
      <p>In 2003 Adrian returned to Sydney to focus on financial services recruitment within the Asia Pacific region, and managing a multi-discipline recruitment division covering recruitment into risk, compliance, law, sales, marketing and corporate advisory.</p>
      <p>Adrian founded Keller Careers in 2011 as a result of client demand for a senior specialist recruitment firm with deep experience in technical markets. His recruitment strategy has involved partnering with high profile Australian and international financial services organisations, and running bespoke recruitment campaigns to identify technical skill sets and high performing professionals from manager to MD level appointments.</p>
      <p>Adrian specialises in recruitment across the disciplines of: Compliance, operational risk, market risk, credit risk, internal audit, and law.</p>
    </div>
  </section>

  <section class="person person--second">
    <div class="portrait" role="img" aria-label="Portrait photo of Nathan Ridley"></div>
    <div class="bio">
      <h2>Nathan Ridley - Director</h2>
      <p>Nathan has extensive experience in both executive search and contingent placement within the APAC region. After graduating from Coastline University with a Bachelor of Commerce, Nathan spent four years in executive search, consulting within the fixed income trading arena, where he specialised in interest rate derivative and credit derivative trading in the Asia Pacific region.</p>
      <p>Having successfully developed and maintained a significant number of high quality relationships within the investment banking industry, Nathan went on to lead a team of recruitment consultants servicing the requirements of investment banks, corporate and retail banks, fund managers and other financial service providers.</p>
      <p>As a proven leader and well-connected executive search professional, Nathan has an excellent reputation in attaining results across a wide variety of assignments.</p>
    </div>
  </section>

  <svg class="footer-art" width="849" height="170" viewBox="0 0 849 170">
    <path fill="var(--navy-soft)" d="M260,130 C470,120 620,55 760,35 C800,30 830,30 849,32 V75 C700,80 540,120 300,135 Z"/>
    <path fill="var(--navy)" d="M0,0 C30,70 110,125 240,132 C450,142 620,68 849,52 V170 H0 Z"/>
  </svg>

  <div class="contact-heading">CONTACT US</div>
  <div class="contact-rule"></div>

  <div class="contact-row">
    <div class="contact-item contact-item--web">
      <svg viewBox="0 0 24 24"><circle cx="12" cy="12" r="12" fill="#fff"/><circle cx="12" cy="12" r="7" fill="none" stroke="#1d4289" stroke-width="1.6"/><ellipse cx="12" cy="12" rx="3" ry="7" fill="none" stroke="#1d4289" stroke-width="1.4"/><line x1="5" y1="12" x2="19" y2="12" stroke="#1d4289" stroke-width="1.4"/></svg>
      <span>kellercareers.com.au</span>
    </div>
    <div class="contact-item contact-item--mail">
      <svg viewBox="0 0 24 24"><circle cx="12" cy="12" r="12" fill="#fff"/><rect x="6" y="8" width="12" height="8.5" rx="1" fill="none" stroke="#1d4289" stroke-width="1.5"/><path d="M6.5 8.5 L12 13 L17.5 8.5" fill="none" stroke="#1d4289" stroke-width="1.5"/></svg>
      <span>info@kellercareers.com.au</span>
    </div>
    <div class="contact-item contact-item--pin">
      <svg viewBox="0 0 24 24"><circle cx="12" cy="12" r="12" fill="#fff"/><path d="M12 5.5 C9 5.5 7.5 7.7 7.5 10 C7.5 13 12 18.5 12 18.5 C12 18.5 16.5 13 16.5 10 C16.5 7.7 15 5.5 12 5.5 Z" fill="#1d4289"/><circle cx="12" cy="10" r="1.8" fill="#fff"/></svg>
      <span>1402/58 Hart St, Sydney, NSW, 2000</span>
    </div>
    <div class="contact-item contact-item--phone">
      <svg viewBox="0 0 24 24"><circle cx="12" cy="12" r="12" fill="#fff"/><path d="M8.6 6.5 L10.4 6.5 L11.2 9.4 L9.9 10.5 C10.6 12 11.9 13.3 13.5 14.1 L14.6 12.8 L17.5 13.6 L17.5 15.4 C17.5 16.3 16.8 17 15.9 17 C11 16.6 7.4 13 7 8.1 C7 7.2 7.7 6.5 8.6 6.5 Z" fill="#1d4289"/></svg>
      <span>+61 (0)2 5550 1847</span>
    </div>
  </div>

</div>
</body>
</html>
```